RM Tomás Ferrier (Business Card)

Hi designers, in this work, I'm looking for an sophisticated stylish, elegant and proffesional personal card. We have a laboratory of pathology automated, with equipments high quality.
In this web the designers, have created my business logo, the name is "RM Tomás Ferrier"
In our lab, we principal work is to prepare the biopsies for further diagnostic of diseases like cancer, tumors, etc.
I need that the first face, only having my complete logo (Rm Tomás Ferrier, Laboratorio de procesamiento Histologico)
The overleaf, could repeat the same logo, like water logo.
In this face, I need to say: My full data:

Técnico en Anatomía Patológica
Tomás Ferrier Bustos M.P 48207
Av. Ramón Quiroga 817 - 2do piso - Instituto Brandeck.
Córdoba, Argentina
(0351) 156284930
ferrier.tomas@correoluz.com

with respect the colors of card, use your imagination, the original logo color is violet, I haven't chosen a color base for the card.

attached pictures are examples of cards I like your DESIGN.
Attached too, the original logo to my company.

the size of card are:
horizontal: 9cm
vertical: 5,5cm

any question that you have, not doubt to question me,
Hand to work!

Industry/Entity Type

Laboratory

Requirements
Must have
• designers sophisticated, not simples, like show the images attached

```html
<!DOCTYPE html>
<html lang="es">
<head>
<meta charset="utf-8">
<title>Tomás Ferrier – Tarjeta personal</title>
<link rel="stylesheet" href="https://fonts.googleapis.com/css2?family=Fira+Sans+Condensed:wght@500&family=Questrial&display=swap">
<style>
  :root {
    --stage: #1c1c1f;
    --violet: #6b24a8;
    --violet-deep: #551a8b;
    --violet-light: #7d34bd;
    --paper: #ffffff;
    --ink-grey: #5c5c5c;
    --white: #ffffff;
  }
  * { margin: 0; padding: 0; box-sizing: border-box; }
  html, body {
    width: 1200px; height: 842px; overflow: hidden;
    background: var(--stage);
  }
  .stage { position: relative; width: 1200px; height: 842px; }
  .card {
    position: absolute; top: 262px;
    width: 520px; height: 318px;
    overflow: hidden;
  }
  .card--front {
    left: 50px;
    background: linear-gradient(135deg, var(--violet-deep), var(--violet-light));
  }
  .card--back { left: 630px; background: var(--paper); }
  .front-watermark {
    position: absolute; left: 28px; top: 22px;
    width: 150px; height: 150px;
    border: 14px solid rgba(0, 0, 0, 0.12);
  }
  .logo {
    position: absolute;
    display: flex; align-items: center; gap: 14px;
    white-space: nowrap;
  }
  .logo__mark { width: 34px; height: 34px; border: 3px solid currentColor; }
  .logo__name {
    font-family: "Fira Sans Condensed", sans-serif;
    font-weight: 500;
    font-size: 34px;
    letter-spacing: 0.22em;
    text-transform: uppercase;
    line-height: 1;
  }
  .tagline {
    position: absolute;
    font-family: "Fira Sans Condensed", sans-serif;
    font-weight: 500;
    text-transform: uppercase;
    line-height: 1;
    white-space: nowrap;
  }
  .card--front .logo { left: 60px; top: 120px; color: var(--white); }
  .card--front .tagline {
    left: 60px; top: 176px; color: var(--white);
    font-size: 21px; letter-spacing: 0.02em;
    padding-top: 10px; border-top: 1.5px solid rgba(255,255,255,0.8);
  }
  .back-band { position: absolute; inset: 0; width: 520px; height: 318px; }
  .card--back .logo { left: 150px; top: 40px; color: var(--ink-grey); }
  .card--back .logo__mark { width: 26px; height: 26px; border-color: var(--violet); border-width: 2.5px; }
  .card--back .logo__name { font-size: 24px; }
  .card--back .tagline {
    left: 150px; top: 80px; color: var(--ink-grey);
    font-size: 16px; letter-spacing: 0.02em;
    padding-top: 6px; border-top: 1px solid var(--ink-grey);
  }
  .details {
    position: absolute; left: 24px; right: 24px; top: 180px;
    color: var(--white);
    font-family: "Questrial", sans-serif;
    text-align: center;
  }
  .details__role { font-size: 13px; letter-spacing: 0.02em; }
  .details__name { font-size: 19px; margin-top: 4px; letter-spacing: 0.02em; }
  .details__address { font-size: 11.5px; margin-top: 8px; }
  .details__contact {
    display: flex; justify-content: center; gap: 28px;
    margin-top: 10px; font-size: 12px;
  }
  .contact-item { display: flex; align-items: center; gap: 7px; }
  .contact-item__icon {
    width: 16px; height: 16px; border-radius: 50%;
    background: var(--white); color: var(--violet);
    font-size: 10px; font-weight: 700;
    display: inline-flex; align-items: center; justify-content: center;
    font-family: "Questrial", sans-serif;
  }
</style>
</head>
<body>
<main class="stage">

  <section class="card card--front" aria-label="Frente de la tarjeta">
    <div class="front-watermark" aria-hidden="true"></div>
    <div class="logo">
      <span class="logo__mark" aria-hidden="true"></span>
      <span class="logo__name">Tomás Ferrier</span>
    </div>
    <p class="tagline">Laboratorio de Procesamiento Histológico</p>
  </section>

  <section class="card card--back" aria-label="Dorso de la tarjeta">
    <svg class="back-band" viewBox="0 0 520 318" aria-hidden="true">
      <path d="M0,118 Q260,122 520,152" fill="none" stroke="var(--violet)" stroke-width="1.5"/>
      <path d="M0,126 Q260,130 520,160" fill="none" stroke="var(--violet)" stroke-width="3"/>
      <path d="M0,136 Q260,140 520,170 L520,318 L0,318 Z" fill="var(--violet)"/>
    </svg>
    <div class="logo">
      <span class="logo__mark" aria-hidden="true"></span>
      <span class="logo__name">Tomás Ferrier</span>
    </div>
    <p class="tagline">Laboratorio de Procesamiento Histológico</p>
    <div class="details">
      <p class="details__role">Técnico en Anatomía Patológica</p>
      <p class="details__name">Tomás Ferrier Bustos M.P 48207</p>
      <p class="details__address">Av. Ramón Quiroga 817 - 2do piso - Instituto Brandeck, Córdoba, Argentina</p>
      <div class="details__contact">
        <span class="contact-item"><span class="contact-item__icon">P</span>(0351) 156284930</span>
        <span class="contact-item"><span class="contact-item__icon">E</span>ferrier.tomas@correoluz.com</span>
      </div>
    </div>
  </section>

</main>
</body>
</html>
```